Employee Benefits and Insurance Consulting

We are an existing company with over 30 years experience but are changing our name. We would like a simple design with grey tones.

Industry/Entity Type

Insurance

Contact Information for Business Card

Marlow Benefits Consulting
Gerald P Odell CEO
5172 Brackenfield Road
Louisville, TN 37777
gerald@marlowbx.com
865-412-3396 - O
865-247-5081 - C

```html
<!DOCTYPE html>
<html lang="en">
<head>
<meta charset="utf-8">
<title>Marlow Benefits Consulting – Business Card</title>
<link href="https://fonts.googleapis.com/css2?family=Montserrat:wght@400;500&display=swap" rel="stylesheet">
<style>
  :root {
    --stage: #e4e4e4;
    --card: #f4f4f4;
    --card-edge: #cfcfcf;
    --ink: #3a3a3a;
    --ink-soft: #5a5a5a;
    --accent: #2d9fdc;
    --band-dark: #2b2b2b;
    --band-mid: #555555;
    --band-light: #8a8a8a;
    --band-text: #f2f2f2;
    --mark: #9a9a9a;
  }
  html, body {
    margin: 0;
    width: 1200px;
    height: 790px;
    overflow: hidden;
    background: var(--stage);
  }
  .business-card {
    position: absolute;
    left: 100px;
    top: 109px;
    width: 1000px;
    height: 572px;
    background: var(--card);
    box-shadow: 0 0 0 1px var(--card-edge), 0 10px 30px rgba(0,0,0,0.18);
    font-family: "Montserrat", sans-serif;
    overflow: hidden;
  }
  .brand {
    position: absolute;
    left: 60px;
    top: 232px;
    display: flex;
    align-items: center;
    gap: 16px;
  }
  .brand-dot {
    width: 46px;
    height: 46px;
    border-radius: 50%;
    background: var(--mark);
  }
  .brand-name {
    font-size: 28px;
    font-weight: 400;
    letter-spacing: 2px;
    color: var(--ink);
    text-transform: uppercase;
  }
  .person {
    position: absolute;
    right: 60px;
    top: 205px;
    text-align: right;
  }
  .person-name {
    font-size: 40px;
    font-weight: 400;
    color: var(--ink-soft);
    letter-spacing: -0.5px;
    text-transform: uppercase;
    line-height: 1;
  }
  .person-title {
    font-size: 16px;
    color: var(--accent);
    margin-top: 6px;
    letter-spacing: 1px;
  }
  .info-band {
    position: absolute;
    left: 0;
    right: 0;
    top: 300px;
    height: 150px;
    background: linear-gradient(90deg, var(--band-dark) 0%, var(--band-mid) 55%, var(--band-light) 100%);
  }
  .address {
    position: absolute;
    left: 60px;
    top: 68px;
    color: var(--band-text);
    font-size: 17px;
    line-height: 1.45;
    text-transform: uppercase;
  }
  .contact {
    position: absolute;
    right: 60px;
    top: 18px;
    color: var(--band-text);
    font-size: 16px;
    line-height: 1.55;
    text-align: right;
    text-transform: uppercase;
  }
  .contact .phones span + span { margin-left: 22px; }
  .footer-strip {
    position: absolute;
    left: 0;
    right: 0;
    top: 450px;
    bottom: 0;
    background: #fafafa;
    border-bottom: 14px solid #5c5c5c;
  }
</style>
</head>
<body>
  <article class="business-card">
    <div class="brand">
      <div class="brand-dot"></div>
      <div class="brand-name">Marlow Benefits Consulting</div>
    </div>

    <div class="person">
      <div class="person-name">Gerald P Odell</div>
      <div class="person-title">CEO</div>
    </div>

    <section class="info-band">
      <div class="address">
        5172 Brackenfield Road<br>
        Louisville, TN 37777
      </div>
      <div class="contact">
        <div class="email">gerald@marlowbx.com</div>
        <div class="phones"><span>(O) (865) 412-3396</span><span>(C) (865) 247-5081</span></div>
      </div>
    </section>

    <div class="footer-strip"></div>
  </article>
</body>
</html>
```